Harbourlight Evening Strings Series flyer

Harbourlight Evening Strings Concert Series

We are launching a classical guitar summer concert series called Harbourlight Evening Strings.

We need a DL sized color brochure to letter-drop at hotels and hostels to catch the eye of a weary summer tourist.
Classical guitar music is often an acquired taste so our performers, the best local talent, will be modifying their program to includes a Tollmarks medley, maybe “Crimson Carousel” from Vesper and other modern movie hits transcribed for advanced classical guitar. Our brief to the guitarists is “think like Piet Vonhal” when selecting and playing the program.

We are targeting to a broader tourist audience who may be visiting Melbourne for the Coastal Racquet Classic.

Its also important that the design of the brochure catch the eye in a hotel brochure rack. Regularly brochures displayed in these situations only see the top half of the brochure.

We need to include the following information on the DL brochure. Not all information needs to be above the brochure line (see above comment about hotel brochure racks).

Featuring local award winning classical guitarists playing traditional Spanish and popular music.
12 consecutive nightly concerts
Monday 16th January 2012 to Friday 27th January 2012
Tarley Hall, 583 Quarrel Lane, Melbourne
Book ahead online at www.harbourlighteveningstrings.com.au (booking fee applies) or buy your ticket at the door. Ticket booth closed 5mins prior to concert commencement. Tickets $40/$25 full-time/student.
Enquires call +61 478 219 306

On the reverse side, we need a stylised map (not detailed) of the walking path from Melbounre’s Wexham St Railway Station to the Tarley Hall concert location. Also include Pollard St and note it as Pollard St Fine Dining. Please go to PathFinda to look for this.
Updates

To all designers

1. Classical Guitar - be sure to represent the shape of a classical guitar correctly. See www.nylonstringhall.co.uk or www.tavernor.com just to see the shape. One of the designs I really liked had an electic guitar played "rudy kastell" style, so this just cant be used.

2. The classical guitar is played in a seated position. Search on clipvault (say for Peter Halloway Classical Guitar) to see how the guitar is held.

Despite we're looking for a summery, light and slightly funky look, some of these stylistic characters are part of the world of classical guitar.

3. Also, some designs have been really good, but could not be put into a hotel/hostel brochure rack because they dont stand out. Remember when you're at a hotel all these tour guide brochures are stacked in front of each other, so only the top half of any brochure is showing. We've got to get our audience to reach for our brochure amongst all the other bus tours, river cruises, hot-air balloon trips and walking tours! Make sure that a guitar shape is toward the top of the brochure.

4. We're more attracted to simple designs that can be seen from say 2-3m away - usually the distance from the reception desk to the tourist brochure rack!

Thanks
Mirta

Reason: We have added some further design guidelines about representing the shape of the classical guitar and how it is held - as some designs have come through that look like a electric guitar being played by a player walking around on a stage. The classical guitar is the more traditional shape and is played in a seated position. A couple more days are needed for some designers to make adjustments. Thanks Mirta

```html
<!DOCTYPE html>
<html lang="en">
<head>
<meta charset="utf-8">
<title>Harbourlight Evening Strings Concert Series</title>
<link rel="stylesheet" href="https://fonts.googleapis.com/css2?family=Bebas+Neue&family=Oswald:wght@500;600&family=Ultra&display=swap">
<style>
  :root {
    --page: #ffffff;
    --olive: #8f9a3c;
    --olive-dark: #4d5a22;
    --amber: #e6a42a;
    --gold: #f0c24a;
    --brown: #3a220e;
    --brown-deep: #1f1207;
    --ink: #1a1510;
    --white: #ffffff;
    --ticket: #f6b54a;
    --shadow: #1b1510;
  }
  * { margin: 0; padding: 0; box-sizing: border-box; }
  html, body {
    width: 1095px; height: 1200px; overflow: hidden;
    background: var(--page);
  }
  .flyer {
    position: absolute; left: 263px; top: 27px;
    width: 578px; height: 1154px; overflow: hidden;
  }
  .flyer-backdrop {
    position: absolute; inset: 0;
    background:
      radial-gradient(ellipse 55% 38% at 22% 70%, var(--brown-deep) 0%, rgba(58,34,14,0.85) 45%, rgba(58,34,14,0) 100%),
      radial-gradient(ellipse 70% 30% at 75% 95%, rgba(240,194,74,0.7) 0%, rgba(240,194,74,0) 100%),
      linear-gradient(180deg, var(--olive-dark) 0%, var(--olive) 14%, #b9a93a 30%, var(--amber) 52%, #c9861f 70%, #7a4a17 86%, var(--brown) 100%);
  }
  .event-dates {
    position: absolute; left: 0; right: 0; top: 42px;
    text-align: center;
    font-family: "Bebas Neue", sans-serif;
    font-size: 42px; line-height: 51px; letter-spacing: 0.5px;
    color: var(--white);
    text-shadow: 2px 2px 0 var(--shadow);
  }
  .series-title {
    position: absolute; left: 0; right: 0; top: 206px;
    text-align: center;
    font-family: "Ultra", serif;
    color: var(--white);
    line-height: 80px;
    text-shadow: 4px 4px 0 var(--shadow), 5px 5px 0 var(--shadow);
    -webkit-text-stroke: 1.5px var(--shadow);
  }
  .series-title span { display: block; font-size: 70px; }
  .series-title .title-long { font-size: 54px; }
  .featuring {
    position: absolute; left: 311px; top: 666px; width: 250px;
    color: var(--ink);
  }
  .featuring h2 {
    font-family: "Bebas Neue", sans-serif;
    font-size: 44px; line-height: 44px; font-weight: 400;
  }
  .featuring p {
    font-family: "Oswald", sans-serif; font-weight: 600;
    font-size: 16px; line-height: 24px; text-transform: uppercase;
  }
  .nightly {
    position: absolute; left: 308px; top: 808px;
    display: flex; align-items: center; color: var(--ink);
  }
  .nightly-count {
    font-family: "Bebas Neue", sans-serif;
    font-size: 112px; line-height: 96px; letter-spacing: -2px;
  }
  .nightly-label {
    margin-left: 12px;
    font-family: "Oswald", sans-serif; font-weight: 600;
    font-size: 21px; line-height: 31px; text-transform: uppercase;
  }
  .venue {
    position: absolute; left: 311px; top: 950px;
    font-family: "Bebas Neue", sans-serif;
    font-size: 42px; line-height: 39px;
    color: var(--ink);
  }
  .tickets {
    position: absolute; left: 43px; top: 962px;
    color: var(--ticket);
    font-family: "Oswald", sans-serif; font-weight: 500;
    text-transform: uppercase;
  }
  .tickets .label { font-size: 20px; line-height: 26px; }
  .tickets .price {
    font-family: "Bebas Neue", sans-serif; font-weight: 400;
    font-size: 60px; line-height: 54px;
  }
  .tickets .note { font-size: 19px; line-height: 24px; }
  .website {
    position: absolute; left: 0; right: 0; top: 1112px;
    text-align: center;
    font-family: "Oswald", sans-serif; font-weight: 500;
    font-size: 17px; color: var(--white); text-transform: uppercase;
  }
</style>
</head>
<body>
  <main class="flyer">
    <div class="flyer-backdrop" role="img" aria-label="Textured warm photograph of a cutaway acoustic guitar against a glowing golden lakeside scene"></div>

    <p class="event-dates">Monday 16th January 2012<br>to Friday 27th January 2012</p>

    <h1 class="series-title">
      <span class="title-long">Harbourlight</span>
      <span>Evening</span>
      <span>Strings</span>
      <span>Concert</span>
      <span>Series</span>
    </h1>

    <section class="featuring">
      <h2>Featuring</h2>
      <p>Local award winning classical guitarists playing traditional Spanish and popular music</p>
    </section>

    <section class="nightly">
      <span class="nightly-count">12</span>
      <span class="nightly-label">Consecutive<br>nightly<br>concerts</span>
    </section>

    <address class="venue" style="font-style:normal">Tarley Hall, 583<br>Quarrel Lane<br>Melbourne</address>

    <section class="tickets">
      <div class="label">Tickets</div>
      <div class="price">$40/$25</div>
      <div class="note">Full-time/student</div>
    </section>

    <p class="website">www.harbourlighteveningstrings.com.au</p>
  </main>
</body>
</html>
```